Corvallin Property Solutions need a business card design

Hello guys. We would need a business card design asap please.
We are a start up property investment business based in London UK specialised in buying, selling, managing and letting properties and helping distressed property owners.
The name of our Business is Corvallin, the logo symbolises the four fundamental elements of the world (earth, air, fire and water) and so it stands for strength, stability, longevity.
We would like the business card to communicate professionalism and reliability. Many many thanks indeed for your work.

Details:

1.) Marisol Dunkley
Property Investor
Mobile: +44(0)7700362517
Email: marisol.corvallin@quilbrook.example

2.) Tomas Brindle
Property Investor
Mobile: +44(0)7700845926
Email: tomas.corvallin@quilbrook.example

Industry/Entity Type

Investment

```html
<!DOCTYPE html>
<html lang="en">
<head>
<meta charset="utf-8">
<title>Corvallin Property Solutions – Business Cards</title>
<link rel="stylesheet" href="https://fonts.googleapis.com/css2?family=Open+Sans:wght@300;400;700&display=swap">
<style>
  :root {
    --bg: #e4e5e8;
    --card: #000000;
    --ink: #ffffff;
    --red: #e8202f;
    --red-light: #ff4c57;
    --green: #1aa33c;
    --green-light: #3fcf62;
    --blue: #2f6fd0;
    --blue-light: #5b95ee;
    --accent: #2f6fd0;
  }
  * { box-sizing: border-box; margin: 0; padding: 0; }
  html, body {
    width: 1200px; height: 800px; overflow: hidden;
    background: var(--bg);
    font-family: "Open Sans", Arial, sans-serif;
  }
  .sheet {
    position: relative; width: 1200px; height: 800px;
    display: flex; align-items: center; justify-content: center; gap: 50px;
  }
  .card {
    position: relative;
    width: 525px; height: 300px;
    background: var(--card);
    color: var(--ink);
    box-shadow: 0 8px 24px rgba(0,0,0,0.18);
    overflow: hidden;
  }
  .band {
    position: absolute; left: 0; right: 0; height: 22px;
    display: flex;
  }
  .band--top { top: 0; }
  .band--bottom { bottom: 0; }
  .band__seg { flex: 1; }
  .band__seg--red   { background: linear-gradient(100deg, var(--red) 0%, var(--red-light) 45%, var(--red) 100%); }
  .band__seg--green { background: linear-gradient(100deg, var(--green) 0%, var(--green-light) 45%, var(--green) 100%); }
  .band__seg--blue  { background: linear-gradient(100deg, var(--blue) 0%, var(--blue-light) 45%, var(--blue) 100%); }

  /* Front */
  .brand {
    position: absolute; left: 120px; top: 118px;
    display: flex; align-items: center; gap: 18px;
  }
  .brand__mark {
    width: 40px; height: 40px; border-radius: 50%;
    background: var(--accent);
  }
  .brand__name {
    font-weight: 700; font-size: 22px; line-height: 1.15;
    letter-spacing: 0.5px; text-transform: uppercase;
    color: var(--ink);
  }

  /* Back */
  .brand--small { left: 70px; top: 70px; gap: 10px; }
  .brand--small .brand__mark { width: 24px; height: 24px; }
  .brand--small .brand__name { font-size: 12px; }

  .contact {
    position: absolute; left: 290px; top: 150px;
    font-size: 11px; line-height: 1.45; font-weight: 400;
  }
  .contact__name {
    font-size: 17px; font-weight: 300; margin-bottom: 3px;
  }
</style>
</head>
<body>
<main class="sheet">

  <section class="card card--front" aria-label="Card front">
    <div class="band band--top">
      <span class="band__seg band__seg--green"></span>
      <span class="band__seg band__seg--red"></span>
      <span class="band__seg band__seg--blue"></span>
      <span class="band__seg band__seg--green"></span>
      <span class="band__seg band__seg--red"></span>
    </div>
    <div class="brand">
      <span class="brand__mark"></span>
      <p class="brand__name">Corvallin<br>Property Solutions</p>
    </div>
    <div class="band band--bottom">
      <span class="band__seg band__seg--red"></span>
      <span class="band__seg band__seg--green"></span>
      <span class="band__seg band__seg--blue"></span>
      <span class="band__seg band__seg--red"></span>
      <span class="band__seg band__seg--green"></span>
    </div>
  </section>

  <section class="card card--back" aria-label="Card back">
    <div class="band band--top">
      <span class="band__seg band__seg--green"></span>
      <span class="band__seg band__seg--red"></span>
      <span class="band__seg band__seg--blue"></span>
      <span class="band__seg band__seg--green"></span>
      <span class="band__seg band__seg--red"></span>
    </div>
    <div class="brand brand--small">
      <span class="brand__mark"></span>
      <p class="brand__name">Corvallin<br>Property Solutions</p>
    </div>
    <div class="contact">
      <p class="contact__name">Marisol Dunkley</p>
      <p class="contact__role">Property Investor</p>
      <p class="contact__phone">Phone:+44(0)7700362517</p>
      <p class="contact__email">Email:marisol.corvallin@quilbrook.example</p>
    </div>
    <div class="band band--bottom">
      <span class="band__seg band__seg--red"></span>
      <span class="band__seg band__seg--green"></span>
      <span class="band__seg band__seg--blue"></span>
      <span class="band__seg band__seg--red"></span>
      <span class="band__seg band__seg--green"></span>
    </div>
  </section>

</main>
</body>
</html>
```